Help me create an amazing cover for my first ebook!!

I am looking to have a modern and professional looking cover for my first ebook. It will be published through Borvex Quill Self Press and will need to follow their formatting and guidelines. I want the cover to have a modern and vibrant feel, that appeals to a millennial audience. This is a real estate book that is focused on a niche category catered to young professionals, so the idea would be to appeal to them.

Title:
The Twentysomething Playbook for Duplex Living

A Smart Property Buying Plan to Start Early, Cut Your Housing Costs (Sometimes to Zero), and Speed Up Your Path to Lasting Wealth.

Davin Osterlund

Target Market(s)

Real Estate investors, investors, millennials, young professionals, college educated, 20-40 years old.Financial freedom, finance.

Industry/Entity Type

Real Estate

Font styles to use
Sans Serif

Colors

Designer to choose colors to be used in the design.

Requirements
Must have
• Must follow the borvex quill self press format. I attached a screenshot of the details, it can also be found here: https://qsp.borvexbooks.example/en_US/help/topic/R481736025
• Must include this title:
• The Twentysomething Playbook for Duplex Living
• A Smart Property Buying Plan to Start Early, Cut Your Housing Costs (Sometimes to Zero), and Speed Up Your Path to Lasting Wealth.
• Davin Osterlund.
• I added examples of book covers I like to use as a guide, I also added some color pallette examples.
Nice to have
• Modern, clean design that's not too busy. Some sort of simple photo or illustration to incorporate in the cover along with the text would be nice.

```html
<!DOCTYPE html>
<html lang="en">
<head>
<meta charset="utf-8">
<title>The Twentysomething Playbook for Duplex Living — Davin Osterlund</title>
<link rel="stylesheet" href="https://fonts.googleapis.com/css2?family=Fredoka:wght@500;600;700&family=Roboto+Condensed:wght@400&display=swap">
<style>
  :root {
    --mint-top: #e6f5dc;
    --mint-mid: #c9ecd0;
    --mint-bottom-a: #b6e7c0;
    --mint-bottom-b: #d6f2cc;
    --slate: #3b424d;
    --slate-light: #4a525e;
    --slate-glow: #56606b;
    --ink: #2c3440;
    --accent: #b9e27a;
    --box-fill: #f4fbe9;
    --line-light: #e8efe6;
  }
  * { margin: 0; padding: 0; box-sizing: border-box; }
  html, body { width: 752px; height: 1200px; overflow: hidden; background: #fff; }
  .cover {
    position: relative;
    width: 752px;
    height: 1200px;
    overflow: hidden;
    font-family: "Fredoka", sans-serif;
    color: var(--ink);
    background: linear-gradient(180deg, var(--mint-top) 0%, var(--mint-mid) 36%);
  }
  .author {
    position: absolute;
    top: 22px; left: 0; right: 0;
    text-align: center;
    font-weight: 500;
    font-size: 33px;
    letter-spacing: 0.5px;
  }
  .series-line {
    position: absolute;
    top: 76px; left: 0; right: 0;
    text-align: center;
    font-weight: 700;
    font-size: 34px;
  }
  .title-heading { font-size: inherit; }
  .title-word {
    position: absolute;
    font-family: "Fredoka", sans-serif;
    font-weight: 700;
    color: var(--ink);
    letter-spacing: 4px;
  }
  .title-word .shade {
    position: absolute;
    left: -18px; top: -9px;
    width: 100%; height: 100%;
    background: var(--accent);
  }
  .title-word .plate {
    position: absolute;
    inset: 0;
    background: var(--box-fill);
    border: 5px solid var(--ink);
    display: flex;
    align-items: center;
    justify-content: center;
    line-height: 1;
  }
  .title-word.first { left: 196px; top: 164px; width: 418px; height: 116px; font-size: 92px; }
  .title-word.second { left: 93px; top: 296px; width: 564px; height: 116px; font-size: 92px; }

  .scene-band {
    position: absolute;
    left: 0; right: 0;
    top: 438px; height: 476px;
    background: var(--slate);
  }
  .scene-art {
    position: absolute;
    left: 38px; right: 38px;
    top: 56px; bottom: 20px;
    background:
      radial-gradient(circle at 88% 14%, rgba(232,239,230,0.22) 0 40px, transparent 70px),
      radial-gradient(ellipse at 50% 85%, var(--slate-glow) 0%, var(--slate-light) 45%, var(--slate) 100%);
    border-radius: 4px;
  }
  .ground-line {
    position: absolute;
    left: 24px; right: 24px; bottom: 18px;
    height: 4px;
    background: var(--line-light);
    border-radius: 2px;
  }

  .tagline {
    position: absolute;
    left: 0; right: 0;
    top: 914px; bottom: 0;
    background: linear-gradient(180deg, var(--mint-bottom-a) 0%, var(--mint-bottom-b) 100%);
    text-align: center;
    padding-top: 24px;
    font-family: "Roboto Condensed", sans-serif;
  }
  .tagline p {
    font-weight: 400;
    font-size: 36px;
    line-height: 50px;
    letter-spacing: 0.3px;
  }
</style>
</head>
<body>
  <main class="cover">
    <p class="author">Davin Osterlund</p>
    <p class="series-line">The Twentysomething Playbook for</p>

    <h1 class="title-heading" aria-label="Duplex Living">
      <span class="title-word first"><span class="shade"></span><span class="plate">DUPLEX</span></span>
      <span class="title-word second"><span class="shade"></span><span class="plate">LIVING</span></span>
    </h1>

    <section class="scene-band">
      <div class="scene-art" role="img" aria-label="Light line illustration of a street of houses, a duplex, a small garage and trees under a sun and clouds"></div>
      <div class="ground-line"></div>
    </section>

    <section class="tagline">
      <p>Speed Up Your Path to Lasting Wealth</p>
      <p>Cut Your Housing Costs (Sometimes to Zero)</p>
      <p>A Smart Property Buying Plan</p>
      <p>to Start Early</p>
    </section>
  </main>
</body>
</html>
```